Need a flyer overhaul and minor changes

flyer is 5.5" x 8.5" we need to change the $250.00 to $325.00, update our company logo on the brochure, and also have an area where we can have the store address (318 W Harlan Ave, Del Rio, TX 78840 - (830) 642-9158). I've attached a our current brochure and our updated logo and we just want to make look better and updated.

Industry/Entity Type

Lending and Finance

Requirements
Nice to have
• updated layout and pictures

```html
<!DOCTYPE html>
<html lang="en">
<head>
<meta charset="utf-8">
<title>Stuck in a Title Loan? – Flyer</title>
<link href="https://fonts.googleapis.com/css2?family=Montserrat:wght@600;700;800;900&family=Poppins:wght@500;600;700&display=swap" rel="stylesheet">
<style>
  :root{
    --red:#c41f2b;
    --green:#1d5f34;
    --white:#ffffff;
    --ink:#1b1b1b;
    --row:#ececec;
    --stage:#5a5a5a;
    --paper-fade:#e4e4e4;
  }
  *{box-sizing:border-box;margin:0;padding:0}
  html,body{width:1200px;height:617px;overflow:hidden}
  body{background:var(--stage);font-family:"Poppins",sans-serif;color:var(--ink);position:relative}

  .flyer{position:absolute;left:412px;top:18px;width:375px;height:580px;
    background:linear-gradient(100deg,var(--white) 55%,var(--paper-fade) 100%);
    box-shadow:0 6px 18px rgba(0,0,0,.35);overflow:hidden}
  .flyer__band{position:absolute;left:0;top:0;width:100%;height:182px;background:var(--red)}
  .flyer__title{position:absolute;left:0;top:16px;width:100%;text-align:center;
    font-family:"Montserrat",sans-serif;font-weight:900;color:var(--white);
    font-size:42px;line-height:40px;letter-spacing:.5px;text-shadow:0 2px 3px rgba(0,0,0,.3)}

  .photo{position:absolute;left:21px;width:139px;height:118px;border-radius:9px}
  .photo--handover{top:117px;background:linear-gradient(160deg,#e9e6e2 0%,#c9a37a 60%,#a8794e 100%)}
  .photo--cash{top:242px;background:radial-gradient(circle at 50% 60%,#8e8a80 0%,#3b3b3d 55%,#1d1d20 100%)}
  .photo--signing{top:367px;background:linear-gradient(150deg,#f2f3f5 0%,#c7ccd4 50%,#6f7788 100%)}

  .compare{position:absolute;left:171px;top:117px;width:183px;height:368px}
  .compare__head{height:26px;background:var(--green);border-radius:10px 10px 0 0;
    color:var(--white);font-weight:600;font-size:12.5px;text-align:center;line-height:26px}
  .compare__body{position:relative;height:296px;background:var(--white);
    border:2px solid var(--green);border-top:none}
  .compare__body::after{content:"";position:absolute;left:93px;top:0;bottom:0;width:1px;background:var(--ink)}
  .compare__cols{display:flex;height:50px}
  .compare__brand{width:94px;display:flex;align-items:center;justify-content:center;text-align:center;
    font-family:"Montserrat",sans-serif;font-weight:700;font-size:10px;line-height:11px;color:var(--green)}
  .compare__label{flex:1;display:flex;align-items:center;justify-content:center;text-align:center;
    font-family:"Montserrat",sans-serif;font-weight:800;font-size:16px;line-height:16px;color:var(--green)}
  .compare__row{display:flex;height:20px;align-items:center;font-weight:600;font-size:11px}
  .compare__row:nth-child(odd){background:var(--row)}
  .compare__num{width:26px;text-align:center;font-weight:500}
  .compare__ours{width:68px}
  .compare__theirs{flex:1;text-align:center}
  .compare__foot{display:flex;height:46px}
  .result{display:flex;flex-direction:column;align-items:center;justify-content:center;
    color:var(--white);font-family:"Montserrat",sans-serif;font-weight:800;line-height:17px}
  .result--paid{width:95px;background:var(--green);border-radius:0 0 0 10px;font-size:18px}
  .result--owe{flex:1;background:var(--red);border-radius:0 0 10px 0;font-size:13px}
  .result--owe strong{font-size:18px;font-weight:800}

  .footer__tab{position:absolute;left:161px;top:490px;width:214px;height:21px;background:var(--red);
    border-radius:10px 0 0 0;color:var(--white);font-weight:600;font-size:13.5px;line-height:21px;padding-left:12px}
  .footer__brand{position:absolute;left:12px;top:522px;width:132px;text-align:center;
    font-family:"Montserrat",sans-serif;font-weight:700;font-size:17px;line-height:19px;color:var(--green)}
  .contact{position:absolute;left:170px;font-weight:600;display:flex;align-items:center;gap:5px;white-space:nowrap}
  .contact svg{flex:none;display:block}
  .contact--phone{top:514px;height:26px;font-size:21px;line-height:26px}
  .contact--address{top:543px;height:13px;font-size:9.5px;line-height:13px}
  .contact--web{top:557px;height:13px;font-size:9.5px;line-height:13px;font-weight:500}
  .contact--web b{font-weight:700}
  .contact--web em{font-style:normal;color:var(--red);font-weight:700}
</style>
</head>
<body>
<main class="flyer">
  <div class="flyer__band"></div>
  <h1 class="flyer__title">STUCK IN A<br>TITLE LOAN?</h1>

  <div class="photo photo--handover" role="img" aria-label="Photo of hands passing a stack of banknotes across a desk"></div>
  <div class="photo photo--cash" role="img" aria-label="Photo of a woman holding a fan of dollar bills"></div>
  <div class="photo photo--signing" role="img" aria-label="Photo of hands signing loan paperwork with a pen"></div>

  <section class="compare">
    <div class="compare__head">$1,000 Loan Comparison</div>
    <div class="compare__body">
      <div class="compare__cols">
        <div class="compare__brand">Northgate<br>Lending</div>
        <div class="compare__label">TITLE<br>LOAN</div>
      </div>
      <div class="compare__rows">
        <div class="compare__row"><span class="compare__num">1</span><span class="compare__ours">$131.67</span><span class="compare__theirs">$325.00</span></div>
        <div class="compare__row"><span class="compare__num">2</span><span class="compare__ours">$131.67</span><span class="compare__theirs">$325.00</span></div>
        <div class="compare__row"><span class="compare__num">3</span><span class="compare__ours">$131.67</span><span class="compare__theirs">$325.00</span></div>
        <div class="compare__row"><span class="compare__num">4</span><span class="compare__ours">$131.67</span><span class="compare__theirs">$325.00</span></div>
        <div class="compare__row"><span class="compare__num">5</span><span class="compare__ours">$131.67</span><span class="compare__theirs">$325.00</span></div>
        <div class="compare__row"><span class="compare__num">6</span><span class="compare__ours">$131.67</span><span class="compare__theirs">$325.00</span></div>
        <div class="compare__row"><span class="compare__num">7</span><span class="compare__ours">$131.67</span><span class="compare__theirs">$325.00</span></div>
        <div class="compare__row"><span class="compare__num">8</span><span class="compare__ours">$131.67</span><span class="compare__theirs">$325.00</span></div>
        <div class="compare__row"><span class="compare__num">9</span><span class="compare__ours">$131.67</span><span class="compare__theirs">$325.00</span></div>
        <div class="compare__row"><span class="compare__num">10</span><span class="compare__ours">$131.67</span><span class="compare__theirs">$325.00</span></div>
        <div class="compare__row"><span class="compare__num">11</span><span class="compare__ours">$131.67</span><span class="compare__theirs">$325.00</span></div>
        <div class="compare__row"><span class="compare__num">12</span><span class="compare__ours">$131.67</span><span class="compare__theirs">$325.00</span></div>
      </div>
    </div>
    <div class="compare__foot">
      <div class="result result--paid"><span>PAID</span><span>OFF</span></div>
      <div class="result result--owe"><span>STILL OWE</span><strong>$1,000</strong></div>
    </div>
  </section>

  <div class="footer__tab">SE HABLA ESPAÑOL</div>
  <div class="footer__brand">Northgate<br>Lending</div>

  <div class="contact contact--phone">
    <svg width="14" height="14" viewBox="0 0 24 24"><path d="M6.6 10.8c1.4 2.8 3.8 5.1 6.6 6.6l2.2-2.2c.3-.3.7-.4 1-.2 1.1.4 2.3.6 3.6.6.6 0 1 .4 1 1V20c0 .6-.4 1-1 1C10.6 21 3 13.4 3 4c0-.6.4-1 1-1h3.5c.6 0 1 .4 1 1 0 1.2.2 2.4.6 3.6.1.3 0 .7-.2 1z" fill="var(--ink)"/></svg>
    <span>(830) 642-9158</span>
  </div>
  <div class="contact contact--address">
    <svg width="9" height="11" viewBox="0 0 9 11"><path d="M4.5 0 A4 4 0 0 1 8.5 4 C8.5 7 4.5 11 4.5 11 C4.5 11 .5 7 .5 4 A4 4 0 0 1 4.5 0 Z" fill="var(--ink)"/><circle cx="4.5" cy="4" r="1.6" fill="var(--white)"/></svg>
    <span>318 W Harlan Ave, Del Rio, TX 78840</span>
  </div>
  <div class="contact contact--web">
    <svg width="10" height="10" viewBox="0 0 10 10" fill="none" stroke="var(--ink)" stroke-width=".9"><circle cx="5" cy="5" r="4.3"/><ellipse cx="5" cy="5" rx="1.9" ry="4.3"/><path d="M.7 5 H9.3 M1.5 2.8 H8.5 M1.5 7.2 H8.5"/></svg>
    <span>Visit us at <b>www.<em>northgatelending</em>.com</b></span>
  </div>
</main>
</body>
</html>
```